Tri Fold - Restaurant Brochure & pdf multipage

Develop a product guide specific to "restaurant owners" for our company's restaurant insurance services. It will need to be eye-catching, personal, unique, and industry-specific. Several Insurance flyers from our companies are attached for review. We are happy to provide guidance along the way. Our website is www.kovalenbrokerage.example. Please grab logos etc. from there. We can provide other files and more detailed copy.

Target Market(s)

Restaurant owners and CFO's

Industry/Entity Type

Insurance Broker

Font styles to use
Other font styles liked:
• match website fonts

Requirements
Must have
• WE WILL PROVIDE DETAILED CONTENT! AT THIS TIME WE ARE LOOKING FOR THE BASIC DESIGN AND LAYOUT.

EYE-CATCHING MODERN DESIGN WITH IMAGES AND BRANDED FEEL. must be print-ready and set up as a PDF to email.

brief description of our agency and its personal boutique feel specializing in the restaurant market. Also, offer a full-service solution to no only manage their business but personal risks too.

Coverages that need to be listed with a brief description: (See attached Flyers)
General Liability
FF&E (Furniture, Fixtures, and Equipment), Property
Workers Compensation
Umbrella
Liquor Liability
Auto
Cyber
Bonds
EPLI

Carrier List:
The Wexmoor
Bastion
Ferrow Common
Wayfarers
Plains Motor
Quorra
DELVA
Holloway
CountyFirst
KTO
And many more
Nice to have
• carrier logos if room.
Should not have
• TO BE DETERMINED.

```html
<!DOCTYPE html>
<html lang="en">
<head>
<meta charset="utf-8">
<title>Kovalen Brokerage – Restaurant Tri-Fold</title>
<link rel="stylesheet" href="https://fonts.googleapis.com/css2?family=Marcellus&family=Open+Sans:wght@400;600;700&display=swap">
<style>
:root{
  --red:#d7262c;
  --red-dark:#b51d22;
  --black:#141414;
  --charcoal:#232323;
  --white:#ffffff;
  --paper:#f4f4f2;
  --ink:#3a3a3a;
  --muted:#bdbdbd;
  --stage:#e8e5e0;
  --head:"Marcellus", Georgia, serif;
  --body:"Open Sans", Arial, sans-serif;
}
*{box-sizing:border-box;margin:0;padding:0}
html,body{width:1200px;height:2400px;overflow:hidden;background:var(--stage)}
.canvas{position:relative;width:1200px;height:2400px;overflow:hidden;font-family:var(--body);color:var(--ink)}
.spread{position:absolute;left:40px;width:1120px;height:1060px;display:flex;box-shadow:0 6px 24px rgba(0,0,0,.18)}
.spread--outside{top:80px}
.spread--inside{top:1260px}
.panel{position:relative;width:373.33px;height:100%;overflow:hidden}
.panel--wide{width:746.67px}
.photo{position:absolute;display:block}

/* brand */
.brand{display:flex;align-items:center;gap:12px;font-family:var(--head);font-size:30px;letter-spacing:1px;color:var(--white);white-space:nowrap}
.brand__mark{width:22px;height:22px;background:var(--red);flex:none}
.brand--dark{color:var(--black)}

/* outside left */
.panel--markets{background:var(--paper)}
.panel--markets .photo{left:0;top:0;width:100%;height:260px;background:linear-gradient(135deg,#7b6a5c,#c9b59a 45%,#e4d6bf 70%,#5a4a3d)}
.markets{position:absolute;top:290px;left:32px;right:30px}
.section-title{font-family:var(--head);color:var(--red);font-size:22px;letter-spacing:1px;text-transform:uppercase;margin-bottom:16px}
.market{margin-bottom:16px}
.market h4{font-size:12.5px;font-weight:700;color:var(--red);text-transform:uppercase;letter-spacing:.4px;margin-bottom:4px}
.market p{font-size:11.5px;line-height:1.5;color:var(--ink)}

/* outside middle */
.panel--about{background:var(--black);color:var(--muted)}
.panel--about .photo{left:50%;top:36px;width:150px;height:150px;margin-left:-75px;border-radius:50%;border:5px solid var(--red);background:radial-gradient(circle at 45% 40%,#d8cfc2,#8c7a66 50%,#2e2620)}
.panel--about .brand{justify-content:center;margin-top:214px;font-size:28px}
.about{padding:0 30px}
.about .section-title{text-align:center;font-size:19px;margin:26px 0 16px}
.about p{font-size:11.5px;line-height:1.6;margin-bottom:12px}
.about p strong{color:var(--white);font-weight:600}
.contact{margin-top:26px;border-top:1px solid #3c3c3c;padding-top:18px}
.contact .section-title{font-size:17px;margin:0 0 14px}
.contact__offices{display:flex;gap:18px}
.office{flex:1;font-size:11px;line-height:1.55}
.office h5{color:var(--red);font-size:11.5px;text-transform:uppercase;letter-spacing:.5px;margin-bottom:4px}
.contact__web{font-size:11.5px;color:var(--white);text-align:center;margin-top:18px}
.license{font-size:10px;color:#8a8a8a;text-align:center;margin-top:8px}

/* cover */
.panel--cover{background:var(--black)}
.panel--cover .brand{position:absolute;top:70px;left:50%;transform:translateX(-50%);font-size:30px}
.cover__photo{left:0;top:190px;width:100%;height:660px;clip-path:polygon(0 9%,100% 0,100% 100%,0 100%);background:linear-gradient(160deg,#c9c2b6,#efece6 35%,#a99a88 60%,#5a4d43)}
.cover__band{position:absolute;left:0;bottom:0;width:100%;height:330px;background:var(--red);clip-path:polygon(0 26%,100% 0,100% 100%,0 100%);padding:118px 26px 0;text-align:center;color:var(--white)}
.cover__kicker{font-family:var(--body);font-weight:700;font-size:12.5px;letter-spacing:.8px;text-transform:uppercase;line-height:1.5}
.cover__headline{font-family:var(--head);font-size:21px;line-height:1.25;letter-spacing:.5px;text-transform:uppercase;margin-top:10px}
.cover__web{display:inline-block;margin-top:20px;background:var(--black);color:var(--white);font-size:11.5px;letter-spacing:.5px;padding:8px 22px}

/* inside left */
.panel--story{background:var(--black);color:var(--muted)}
.story{padding:44px 30px 0}
.story .section-title{font-size:20px;line-height:1.2;margin-bottom:14px}
.story p{font-size:11.5px;line-height:1.6;margin-bottom:11px}
.lists{display:flex;gap:18px;margin-top:20px}
.lists__col{flex:1}
.lists h4{font-family:var(--head);color:var(--red);font-size:15px;letter-spacing:1px;text-transform:uppercase;margin-bottom:8px}
.lists ul{list-style:none;font-size:11.5px;line-height:1.65;color:var(--white)}
.lists li::before{content:"";display:inline-block;width:5px;height:5px;background:var(--red);margin-right:8px;vertical-align:middle}
.story__photo{left:0;bottom:0;width:100%;height:260px;clip-path:ellipse(120% 100% at 50% 100%);background:linear-gradient(135deg,#3b332d,#b9ab98 45%,#efe9df 60%,#6d5e50)}
.story__edge{position:absolute;left:0;bottom:252px;width:100%;height:20px}

/* inside right spread */
.panel--coverages{background:var(--white)}
.coverages__photo{left:0;top:0;width:100%;height:410px;background:linear-gradient(120deg,#3a2f28,#8a735f 35%,#d6c7b2 60%,#6a574a 80%,#2c241f)}
.coverages__brand{position:absolute;top:130px;right:40px;background:rgba(255,255,255,.9);padding:10px 16px}
.coverages__brand .brand{font-size:24px}
.coverages__band{position:absolute;left:0;top:380px;width:100%;height:60px;background:var(--white);clip-path:polygon(0 55%,100% 0,100% 100%,0 100%)}
.coverages__body{position:absolute;top:440px;left:34px;right:34px;display:flex;gap:34px}
.coverages__col{flex:1}
.coverages__title{font-family:var(--head);color:var(--red);font-size:19px;line-height:1.2;text-transform:uppercase;letter-spacing:.5px;margin-bottom:10px}
.coverages__intro{font-size:11.5px;line-height:1.55;margin-bottom:16px}
.coverage{display:flex;gap:12px;margin-bottom:14px}
.coverage__icon{flex:none;width:38px;height:38px;border:2px solid var(--red);display:flex;align-items:center;justify-content:center}
.coverage__icon svg{width:22px;height:22px;stroke:var(--charcoal);fill:none;stroke-width:1.6;stroke-linecap:round;stroke-linejoin:round}
.coverage h4{font-size:12px;font-weight:700;color:var(--red);text-transform:uppercase;letter-spacing:.3px;margin-bottom:3px}
.coverage p{font-size:11px;line-height:1.5}
.cta{position:absolute;right:0;bottom:0;width:373px;height:118px;background:var(--red);clip-path:polygon(0 22%,100% 0,100% 100%,0 100%);color:var(--white);padding:44px 28px 0;text-align:right}
.cta__line{font-weight:700;font-size:12px;letter-spacing:.6px;text-transform:uppercase}
.cta__call{margin-top:8px;font-size:14px;display:flex;justify-content:flex-end;align-items:center;gap:8px}
.cta__call svg{width:14px;height:14px;fill:var(--white)}
</style>
</head>
<body>
<main class="canvas">

  <!-- Outside of tri-fold -->
  <section class="spread spread--outside">

    <article class="panel panel--markets">
      <div class="photo" role="img" aria-label="Photo of a smiling restaurant owner serving plated food"></div>
      <div class="markets">
        <h3 class="section-title">What Markets Offer</h3>
        <div class="market"><h4>Competitive Pricing</h4><p>We compare many carriers to find strong coverage at a fair, steady premium for your kitchen.</p></div>
        <div class="market"><h4>Broad Coverage Forms</h4><p>Policies written for food service, from spoilage and equipment breakdown to guest injury.</p></div>
        <div class="market"><h4>Claims Advocacy</h4><p>When something goes wrong, we stand beside you and push for a fast, fair outcome.</p></div>
        <div class="market"><h4>Risk Management</h4><p>Practical checklists and staff training ideas that help reduce losses before they happen.</p></div>
        <div class="market"><h4>Personal Lines</h4><p>Home, auto and life protection for owners, so your family is covered as well as your business.</p></div>
      </div>
    </article>

    <article class="panel panel--about">
      <div class="photo" role="img" aria-label="Round photo of a chef plating a dish in a kitchen"></div>
      <div class="brand"><span class="brand__mark"></span>Kovalen Brokerage</div>
      <div class="about">
        <h3 class="section-title">Business Owner &amp; Personal Risks</h3>
        <p>As a boutique agency we know our clients by name. <strong>Restaurants are our specialty</strong>, and we build every program around the way you actually operate.</p>
        <p>We also look after the owner behind the business, offering one trusted partner for <strong>commercial and personal</strong> insurance needs.</p>
        <p>Ask us for a full review of your current policies and a clear plan for what comes next.</p>
        <div class="contact">
          <h3 class="section-title">Contact Us</h3>
          <div class="contact__offices">
            <div class="office"><h5>Elmsford</h5>118 Larchmont Row<br>Elmsford, ST 30161<br>555-014-2290</div>
            <div class="office"><h5>Dunmere</h5>42 Quarry Lane<br>Dunmere, ST 30303<br>555-014-2291</div>
          </div>
          <p class="contact__web">www.kovalenbrokerage.example</p>
          <p class="license">Licensed in all states we serve · Lic. No. 000000</p>
        </div>
      </div>
    </article>

    <article class="panel panel--cover">
      <div class="brand"><span class="brand__mark"></span>Kovalen Brokerage</div>
      <div class="photo cover__photo" role="img" aria-label="Photo of a smiling chef in whites with arms crossed in a busy kitchen"></div>
      <div class="cover__band">
        <p class="cover__kicker">Small Commercial<br>Small Business Owners / Restaurants</p>
        <h1 class="cover__headline">You work hard serving others.<br>Here's how we can serve you.</h1>
        <span class="cover__web">www.kovalenbrokerage.example</span>
      </div>
    </article>
  </section>

  <!-- Inside of tri-fold -->
  <section class="spread spread--inside">

    <article class="panel panel--story">
      <div class="story">
        <h2 class="section-title">Kovalen Brokerage Loves Restaurants</h2>
        <p>Starting in the hospitality world ourselves, we learned first hand what it takes to keep doors open, staff paid and guests happy every single night.</p>
        <p>That is why we focus on restaurant owners, from corner cafés to multi-unit groups, and shape coverage to the risks of each concept.</p>
        <p>Our carriers compete for your business, and we manage the details so you can stay in the dining room.</p>
        <div class="lists">
          <div class="lists__col">
            <h4>Carriers</h4>
            <ul>
              <li>The Wexmoor</li><li>Bastion</li><li>Ferrow Common</li><li>Wayfarers</li><li>Plains Motor</li><li>Quorra</li><li>DELVA</li><li>Holloway</li><li>CountyFirst</li><li>KTO</li><li>And many more</li>
            </ul>
          </div>
          <div class="lists__col">
            <h4>Coverages</h4>
            <ul>
              <li>General Liability</li><li>FF&amp;E, Property</li><li>Workers Comp</li><li>Umbrella</li><li>Liquor Liability</li><li>Auto</li><li>Cyber</li><li>Bonds</li><li>EPLI</li>
            </ul>
          </div>
        </div>
      </div>
      <svg class="story__edge" viewBox="0 0 373 20" preserveAspectRatio="none" aria-hidden="true"><path d="M0 20 Q186 -6 373 20" fill="none" stroke="#d7262c" stroke-width="6"/></svg>
      <div class="photo story__photo" role="img" aria-label="Photo of a chef preparing food at a kitchen counter"></div>
    </article>

    <article class="panel panel--wide panel--coverages">
      <div class="photo coverages__photo" role="img" aria-label="Photo of guests laughing and dining together at a restaurant table"></div>
      <div class="coverages__brand"><div class="brand brand--dark"><span class="brand__mark"></span>Kovalen Brokerage</div></div>
      <div class="coverages__band"></div>
      <div class="coverages__body">
        <div class="coverages__col">
          <h2 class="coverages__title">Examples of à la carte coverages restaurants like yours select</h2>
          <p class="coverages__intro">A wide range of options lets you build a program that fits your menu, your staff and your budget.</p>
          <div class="coverage">
            <div class="coverage__icon"><svg viewBox="0 0 24 24"><path d="M12 3l8 3v6c0 5-4 8-8 9-4-1-8-4-8-9V6z"/></svg></div>
            <div><h4>General Liability</h4><p>Guest slips, falls and injuries on your premises.</p></div>
          </div>
          <div class="coverage">
            <div class="coverage__icon"><svg viewBox="0 0 24 24"><path d="M3 21V9l9-6 9 6v12z"/><path d="M9 21v-6h6v6"/></svg></div>
            <div><h4>FF&amp;E, Property</h4><p>Furniture, fixtures, equipment and the building.</p></div>
          </div>
          <div class="coverage">
            <div class="coverage__icon"><svg viewBox="0 0 24 24"><circle cx="12" cy="7" r="4"/><path d="M4 21c0-4 4-7 8-7s8 3 8 7"/></svg></div>
            <div><h4>Workers Compensation</h4><p>Medical costs and lost wages for injured staff.</p></div>
          </div>
          <div class="coverage">
            <div class="coverage__icon"><svg viewBox="0 0 24 24"><path d="M3 12a9 9 0 0 1 18 0z"/><path d="M12 12v7a2 2 0 0 1-4 0"/></svg></div>
            <div><h4>Umbrella</h4><p>Extra limits above your primary policies.</p></div>
          </div>
          <div class="coverage">
            <div class="coverage__icon"><svg viewBox="0 0 24 24"><path d="M7 3h10l-1 8a4 4 0 0 1-8 0z"/><path d="M12 15v6M8 21h8"/></svg></div>
            <div><h4>Liquor Liability</h4><p>Claims tied to serving alcohol to guests.</p></div>
          </div>
        </div>
        <div class="coverages__col">
          <p class="coverages__intro">We make it easy to add only what you need, with clear terms and no surprises at renewal time.</p>
          <div class="coverage">
            <div class="coverage__icon"><svg viewBox="0 0 24 24"><path d="M3 16V11l2-5h14l2 5v5z"/><circle cx="7" cy="17" r="2"/><circle cx="17" cy="17" r="2"/></svg></div>
            <div><h4>Auto</h4><p>Delivery and company vehicles on the road.</p></div>
          </div>
          <div class="coverage">
            <div class="coverage__icon"><svg viewBox="0 0 24 24"><rect x="5" y="11" width="14" height="10"/><path d="M8 11V7a4 4 0 0 1 8 0v4"/></svg></div>
            <div><h4>Cyber</h4><p>Data breaches and card payment system attacks.</p></div>
          </div>
          <div class="coverage">
            <div class="coverage__icon"><svg viewBox="0 0 24 24"><rect x="4" y="3" width="16" height="18"/><path d="M8 9h8M8 13h8M8 17h5"/></svg></div>
            <div><h4>Bonds</h4><p>License, permit and contract bonds as required.</p></div>
          </div>
          <div class="coverage">
            <div class="coverage__icon"><svg viewBox="0 0 24 24"><circle cx="8" cy="8" r="3"/><circle cx="16" cy="8" r="3"/><path d="M2 20c0-3 3-5 6-5s6 2 6 5M14 15c3 0 8 1 8 5"/></svg></div>
            <div><h4>EPLI</h4><p>Employment practices claims from staff.</p></div>
          </div>
        </div>
      </div>
      <div class="cta">
        <p class="cta__line">Exceptional coverages don't stop here</p>
        <p class="cta__call"><strong>Call us today</strong>
          <svg viewBox="0 0 24 24" aria-hidden="true"><path d="M6.6 10.8a15 15 0 0 0 6.6 6.6l2.2-2.2a1 1 0 0 1 1-.25 11 11 0 0 0 3.6.6 1 1 0 0 1 1 1V20a1 1 0 0 1-1 1A17 17 0 0 1 3 4a1 1 0 0 1 1-1h3.5a1 1 0 0 1 1 1 11 11 0 0 0 .6 3.6 1 1 0 0 1-.25 1z"/></svg>
          555-014-2290</p>
      </div>
    </article>
  </section>

</main>
</body>
</html>
```